Corwynfel - Business card with logo

Business card with logo. I am an entrepreneur with serveral businesses, this is my personal company, through which I talk to company suppliers as well as customers. I am looking for a sleek design which could easily be upgraded to be used on other company collateral as required ie Email footers, stationery etc

Target Market(s)

Third party suppliers and customers of my own.

Industry/Entity Type

Business Management

Contact Information for Business Card

Lucas Fenwright
Director
lucas@corwynfel.com
07839206417

Font styles to use
Sans Serif

Colors
000000
ffffff
959595

Requirements
Must have
• a nice logo see attached. And the company name Corwynfel. Corwynfel means 'Little Birds' in Welsh which reflects my daughter and I. I would like something with two birds on a wire (see attached PDF for ideas)
• I want to conclude this ASAP I am currently trying to move deadline from 10 to 3 days.
Nice to have
• Happy to see something in colour if you have any good ideas.
Should not have
• Nothing too cartoony please

```html
<!DOCTYPE html>
<html lang="en">
<head>
<meta charset="utf-8">
<title>Corwynfel – Business Card</title>
<link rel="stylesheet" href="https://fonts.googleapis.com/css2?family=Open+Sans:wght@300;400;600;700&display=swap">
<style>
  :root {
    --ink: #000000;
    --paper: #ffffff;
    --grey: #959595;
    --grey-soft: #e6e6e6;
    --bleed: #e8779e;
    --trim: #bdbdbd;
  }
  * { margin: 0; padding: 0; box-sizing: border-box; }
  html, body {
    width: 849px; height: 1200px; overflow: hidden;
    background: var(--paper);
    font-family: "Open Sans", Arial, sans-serif;
    color: var(--ink);
  }
  .sheet { position: relative; width: 849px; height: 1200px; }

  .spec-title {
    position: absolute; top: 104px; left: 0; width: 100%;
    text-align: center; font-weight: 700; font-size: 19px;
  }
  .legend {
    position: absolute; top: 134px; left: 338px;
    font-size: 16px; line-height: 25px;
  }
  .legend-row { display: flex; align-items: center; gap: 12px; }
  .legend-swatch { width: 40px; height: 2px; }
  .legend-swatch.bleed { background: var(--bleed); }
  .legend-swatch.trim { background: var(--trim); }

  .card {
    position: absolute; left: 235px; width: 382px; height: 238px;
    border: 1.5px solid var(--bleed);
  }
  .card::after {
    content: ""; position: absolute; inset: 9px;
    border: 1px solid var(--trim); pointer-events: none;
  }
  .card-front {
    top: 316px;
    background: radial-gradient(ellipse at 50% 48%, var(--paper) 30%, var(--grey-soft) 100%);
  }
  .card-back { top: 698px; background: var(--paper); }

  .brand { display: flex; align-items: center; gap: 7px; color: var(--grey); font-weight: 400; }
  .brand-dot { width: 9px; height: 9px; border-radius: 50%; background: var(--ink); }

  .card-front .brand {
    position: absolute; top: 107px; left: 128px; font-size: 15px; letter-spacing: 0.5px;
  }
  .card-back .brand {
    position: absolute; top: 58px; left: 46px; font-size: 11px;
  }

  .contact {
    position: absolute; right: 30px; bottom: 44px; text-align: right;
  }
  .contact-name { font-weight: 700; font-size: 15px; line-height: 18px; }
  .contact-role { font-weight: 600; font-size: 10px; line-height: 14px; }
  .contact-detail {
    margin-top: 11px; font-weight: 300; font-size: 10px; line-height: 13px; color: var(--grey);
  }
</style>
</head>
<body>
<main class="sheet">
  <h1 class="spec-title">Document size 91mm x 55mm</h1>
  <div class="legend">
    <div class="legend-row"><span class="legend-swatch bleed"></span>Full Bleed Size</div>
    <div class="legend-row"><span class="legend-swatch trim"></span>Document size</div>
  </div>

  <section class="card card-front" aria-label="Card front">
    <div class="brand"><span class="brand-dot"></span>Corwynfel</div>
  </section>

  <section class="card card-back" aria-label="Card back">
    <div class="brand"><span class="brand-dot"></span>Corwynfel</div>
    <div class="contact">
      <p class="contact-name">Lucas Fenwright</p>
      <p class="contact-role">Director</p>
      <p class="contact-detail">lucas@corwynfel.com<br>07839206417</p>
    </div>
  </section>
</main>
</body>
</html>
```